Buch-/E-Book-Cover für Sachbuch über Hunderasse
Zielgruppe
Ich benötige ein Buch-Cover im DIN A5 Format für ein anspruchsvolles Sachbuch, das die rassetypischen Krankheiten der Hunderasse Rhodesian Ridgeback thematisiert. Die Zielgruppe sind Züchter, Tierärzte und Liebhaber der Rasse.
Aufgabenstellung
Den größten Raum sollte ein Foto der Rasse einnehmen. Das Foto würde ich stellen, im Entwurf kann also ein Beispielfoto verwendet werden. Da das Buch der Auftakt zu einer Reihe ist, sollte das Design einen hohen Wiedererkennungswert haben und in erster Linie seriös wirken. Das Foto, der Rassename und die verwendeten Farben sollten leicht austauschbar sein. Sowohl der Titel als auch der Untertitel sind recht lang. Der Arbeitstitel lautet: Stille Pfade im Nebel der Ostseeküste, Untertitel: Geschichten von Fischern und Leuchttürmen.

```html
<!DOCTYPE html>
<html lang="de">
<head>
<meta charset="utf-8">
<title>Stille Pfade im Nebel der Ostseeküste – Buchumschlag</title>
<link rel="stylesheet" href="https://fonts.googleapis.com/css2?family=Catamaran:wght@300;400&display=swap">
<style>
  :root {
    --cover-brown: #75401e;
    --accent-orange: #e8501a;
    --subtitle-orange: #f27d1e;
    --paper: #ffffff;
    --ink-light: #ffffff;
    --photo-light: #d99a52;
    --photo-mid: #b8692e;
    --photo-dark: #8a4a22;
  }
  * { margin: 0; padding: 0; box-sizing: border-box; }
  html, body {
    width: 1200px; height: 821px; overflow: hidden;
    background: var(--paper);
    font-family: "Catamaran", sans-serif;
  }
  .canvas { position: relative; width: 1200px; height: 821px; }
  .book-spread {
    position: absolute; left: 63px; top: 74px; width: 1076px; height: 671px;
    box-shadow: 6px 8px 14px rgba(0,0,0,.35);
  }
  .back-cover {
    position: absolute; left: 0; top: 0; width: 519px; height: 671px;
    background: var(--cover-brown); color: var(--ink-light);
  }
  .back-title {
    position: absolute; left: 100px; top: 96px;
    font-weight: 300; font-size: 33px; line-height: 39px; letter-spacing: -.2px;
  }
  .back-subtitle {
    position: absolute; left: 101px; top: 176px;
    font-weight: 300; font-size: 16.5px;
  }
  .back-blurb {
    position: absolute; left: 99px; top: 230px; width: 300px;
    font-weight: 300; font-size: 13.5px; line-height: 17.8px;
  }
  .isbn {
    position: absolute; left: 110px; top: 598px;
    font-weight: 300; font-size: 10.5px;
  }
  .spine {
    position: absolute; left: 519px; top: 0; width: 24px; height: 671px;
    background: var(--cover-brown);
    border-left: 1px solid rgba(255,255,255,.35);
    border-right: 1px solid rgba(255,255,255,.35);
  }
  .spine-text {
    position: absolute; left: 12px; top: 671px;
    transform-origin: 0 0; transform: rotate(-90deg) translateY(-50%);
    white-space: nowrap; color: var(--ink-light);
    font-size: 11.5px; font-weight: 400; line-height: 1;
    padding-left: 34px;
  }
  .spine-text .spine-sub { margin-left: 22px; font-weight: 300; }
  .front-cover {
    position: absolute; left: 543px; top: 0; width: 533px; height: 671px;
    background: var(--paper); overflow: hidden;
  }
  .cover-photo {
    position: absolute; left: 78px; top: 60px; width: 390px; height: 611px;
    border-radius: 45% 45% 8% 8% / 25% 25% 4% 4%;
    background: radial-gradient(ellipse at 50% 35%, var(--photo-light) 0%, var(--photo-mid) 55%, var(--photo-dark) 100%);
  }
  .title-band {
    position: absolute; left: 0; top: 474px; width: 533px; height: 155px;
    background: var(--cover-brown);
  }
  .accent-bar {
    position: absolute; left: 40px; top: 1px; width: 8px; height: 152px;
    background: var(--accent-orange);
  }
  .front-title {
    position: absolute; left: 83px; top: 17px;
    color: var(--ink-light); font-weight: 300; font-size: 36px; line-height: 42px; letter-spacing: -.2px;
  }
  .front-subtitle {
    position: absolute; left: 84px; top: 110px;
    color: var(--subtitle-orange); font-weight: 300; font-size: 18px;
  }
</style>
</head>
<body>
<main class="canvas">
  <section class="book-spread">
    <article class="back-cover">
      <h2 class="back-title">Stille Pfade im Nebel<br>der Ostseeküste</h2>
      <p class="back-subtitle">Geschichten von Fischern und Leuchttürmen</p>
      <p class="back-blurb">Den größten Raum sollte ein Foto der Rasse einnehmen. Das Foto würde ich stellen, im Entwurf kann also ein Beispielfoto verwendet werden. Da das Buch der Auftakt zu einer Reihe ist, sollte das Design einen hohen Wiedererkennungswert haben und in erster Linie seriös wirken. Das Foto, der Rassename und die verwendeten Farben sollten leicht austauschbar sein. Sowohl der Titel als auch der Untertitel sind recht lang. Der Arbeitstitel lautet: Stille Pfade im Nebel der Ostseeküste, Untertitel: Geschichten von Fischern und Leuchttürmen.</p>
      <p class="isbn">ISBN 1234567889</p>
    </article>
    <div class="spine">
      <p class="spine-text"><span class="spine-title">Stille Pfade im Nebel der Ostseeküste</span><span class="spine-sub">Geschichten von Fischern und Leuchttürmen</span></p>
    </div>
    <article class="front-cover">
      <div class="cover-photo" role="img" aria-label="Porträtfoto eines rotbraunen Hundes vor weißem Hintergrund"></div>
      <div class="title-band">
        <span class="accent-bar"></span>
        <h1 class="front-title">Stille Pfade im Nebel<br>der Ostseeküste</h1>
        <p class="front-subtitle">Geschichten von Fischern und Leuchttürmen</p>
      </div>
    </article>
  </section>
</main>
</body>
</html>
```